Property Development Business Cards

I need a business card design for Tallow Creek Developments Pty Ltd. We are a property development company in Australia and our name defines the five values that we adhere to, being Profitable, Partnerships, Quality Developments, Eco Friendly and Enduring Design.

I have attached the current logo that I use, it is just five yellow circles connected to a single cricle in the middle.

Target Market(s)

Our Target audience is real estate agents, owners of properties, builders and other trades

Industry/Entity Type

Business

Requirements
Must have
• Want to have two sides to the card, one with details and one to just highlight the company

```html
<!DOCTYPE html>
<html lang="en">
<head>
<meta charset="utf-8">
<title>Tallow Creek Developments Pty Ltd — Business Card</title>
<link rel="stylesheet" href="https://fonts.googleapis.com/css2?family=Cabin:wght@500&family=Archivo+Narrow&family=Arimo&display=swap">
<style>
  :root {
    --purple: #7b3f98;
    --blue: #1479d6;
    --blue-light: #bcdcf5;
    --sky: #7ab7ea;
    --ink: #111111;
    --rule: #c8c8c8;
    --yellow: #fbc52a;
    --paper: #ffffff;
  }
  html, body {
    margin: 0;
    padding: 0;
    width: 1013px;
    height: 1200px;
    overflow: hidden;
    background: var(--paper);
  }
  .sheet {
    position: relative;
    width: 1013px;
    height: 1200px;
  }
  .card {
    position: absolute;
    left: 0;
    width: 1013px;
    overflow: hidden;
    background: var(--paper);
  }
  .card--front { top: 0; height: 590px; }
  .card--back { top: 606px; height: 579px; border-right: 3px solid var(--purple); box-sizing: border-box; }
  .band {
    position: absolute;
    left: 0;
    width: 1013px;
    background: var(--purple);
  }
  .band--top { top: 0; height: 10px; }
  .band--middle { top: 590px; height: 16px; }
  .band--bottom { top: 1185px; height: 15px; }
  .shape { position: absolute; left: 0; top: 0; }
  .house-illustration {
    position: absolute;
    left: 540px;
    top: 19px;
    width: 459px;
    height: 227px;
    border-radius: 40px;
    background: radial-gradient(ellipse at 55% 50%, #b87a55 0%, #d9dde2 45%, #eef4fa 75%, rgba(255,255,255,0) 100%);
  }
  .logo-dot {
    position: absolute;
    border-radius: 50%;
    background: var(--yellow);
  }
  .logo-dot--front { left: 160px; top: 168px; width: 60px; height: 60px; }
  .logo-dot--back { left: 479px; top: 656px; width: 42px; height: 42px; }
  .company-name {
    position: absolute;
    margin: 0;
    font-family: "Cabin", sans-serif;
    font-weight: 500;
    color: var(--ink);
    white-space: nowrap;
    border-bottom: 1px solid var(--rule);
    text-align: center;
  }
  .company-name--front {
    left: 110px;
    top: 262px;
    width: 860px;
    font-size: 46px;
    line-height: 62px;
  }
  .company-name--back {
    left: 200px;
    top: 763px;
    width: 620px;
    font-size: 33px;
    line-height: 38px;
  }
  .website {
    position: absolute;
    right: 24px;
    top: 552px;
    margin: 0;
    font-family: "Arimo", sans-serif;
    font-size: 21px;
    color: var(--sky);
  }
  .floral-ornament {
    position: absolute;
    left: 34px;
    top: 608px;
    width: 212px;
    height: 222px;
    border-radius: 50%;
    background: radial-gradient(ellipse at center, rgba(74,152,226,0.45) 0%, rgba(74,152,226,0.12) 60%, rgba(255,255,255,0) 100%);
  }
  .mission {
    position: absolute;
    left: 10px;
    top: 856px;
    width: 993px;
    margin: 0;
    font-family: "Archivo Narrow", sans-serif;
    font-size: 22px;
    line-height: 52px;
    color: var(--ink);
    text-align: center;
  }
</style>
</head>
<body>
<main class="sheet">
  <div class="band band--top"></div>

  <section class="card card--front" aria-label="Front of card">
    <svg class="shape" width="1013" height="590" viewBox="0 0 1013 590" aria-hidden="true">
      <path d="M0 10 H80 C45 150 55 400 190 590 H0 Z" fill="var(--blue-light)"/>
      <path d="M0 10 H72 C35 150 45 400 176 590 H0 Z" fill="var(--blue)"/>
    </svg>
    <div class="house-illustration" role="img" aria-label="Illustration of a two-storey house with terracotta roof standing on rolled architectural plans against soft clouds"></div>
    <span class="logo-dot logo-dot--front" aria-hidden="true"></span>
    <h1 class="company-name company-name--front">Tallow Creek Developments Pty Ltd.</h1>
    <p class="website">www.tallowcreekdevelopments.com.au</p>
  </section>

  <div class="band band--middle"></div>

  <section class="card card--back" aria-label="Back of card">
    <svg class="shape" width="1013" height="579" viewBox="0 0 1013 579" aria-hidden="true">
      <path d="M0 490 C250 590 700 560 1010 440 V579 H0 Z" fill="var(--blue-light)"/>
      <path d="M0 500 C250 590 720 570 1010 455 V579 H0 Z" fill="var(--blue)"/>
    </svg>
  </section>
  <div class="floral-ornament" role="img" aria-label="Blue floral swirl ornament"></div>
  <span class="logo-dot logo-dot--back" aria-hidden="true"></span>
  <h2 class="company-name company-name--back">Tallow Creek Developments Pty Ltd.</h2>
  <p class="mission">Tallow Creek Developments Pty Ltd is committed to quality real estate developments by creating win-win outcomes for all involved. We strongly believe in providing professional functional eco conscious designs to satisfy the changing needs of today's population that will endure in design.</p>

  <div class="band band--bottom"></div>
</main>
</body>
</html>
```